WP website design (Brantow)

We need a wordpress design for an established auction and real estate company based in Kentucky. The winning design will incorporate a professional color scheme with company logo in a clean layout with specified widgets. The design needs to consider that this will be developed on a responsive theme. Colors will complement the colors in the logo.

Industry/Entity Type

Real Estate

Font styles to use
Sans Serif

Requirements
Must have
• - Navigation:
1) Home 2) Auctions 3) Real Estate Listings 4) Our Services 5) Why Auctions 6) About Us 7) Past Auctions 8) Contact Us

Homeage will have slideshow, please use stock real estate image as the initial slide. Homepage will have this content: "Martin Brantow Auctioneer Real Estate Broker

Buying or selling you can count on Martin Brantow Auctioneer to deliver a quality auction experience. We handle all the details from initial handshake to final payment. We are with you every step of the way giving our sellers the service and results they deserve. You only have one chance for a successful auction. Contact us today to see how our experience and know-how can work for you. We are confident that you will appreciate our higher standard of service."

Footer will have smaller company logo, and attached association logos and this contact info:
Phone: (270) 555-0148
Contacts: Martin Brantow
Email: martinbrantow@mailvex.example
Address: 482 Wexcombe Lane • Bowling Green, KY 42190

Widgets:
1) email sign up 2) Social media (twitter, Youtube - can also be in header 3) News & Events Blog widget 4) testimonials blog 5) Featured Video widget
Nice to have
• Nice to Have:
- demonstrate the drop-down menu styling, e.g. under Auctions
-Upcoming Auctions
-Online Auctions
-Past Auctions

```html
<!DOCTYPE html>
<html lang="en">
<head>
<meta charset="utf-8">
<title>Martin Brantow Auctioneer – Home</title>
<link rel="stylesheet" href="https://fonts.googleapis.com/css2?family=Arimo:wght@400;700&family=Ubuntu:wght@400;500;700&display=swap">
<style>
  :root{
    --blue:#1b5aa6;
    --blue-dark:#164c8f;
    --yellow:#f5c211;
    --ink:#333333;
    --muted:#555555;
    --line:#d6d6d6;
    --footer:#4a4a4a;
    --white:#ffffff;
  }
  *{box-sizing:border-box;margin:0;padding:0}
  html,body{width:900px;height:1200px;overflow:hidden;background:var(--white)}
  body{position:relative;font-family:"Arimo",Arial,sans-serif;color:var(--ink)}
  .abs{position:absolute}

  /* header */
  .brand{left:76px;top:12px;display:flex;align-items:center;gap:8px}
  .brand-mark{width:18px;height:18px;background:var(--yellow)}
  .brand-name{font-family:"Ubuntu",sans-serif;font-weight:700;font-size:20px;color:var(--blue);line-height:1.1;width:110px}
  .signup{left:386px;top:18px;width:438px;height:53px;background:var(--blue);border-radius:3px;display:flex;align-items:center;padding:0 12px;gap:13px}
  .signup-field{width:164px;height:26px;background:var(--white);border-radius:4px;font-size:11px;color:var(--ink);padding:7px 18px}
  .signup-field.email{padding-left:10px}
  .signup-btn{margin-left:2px;width:57px;height:24px;background:var(--yellow);border-radius:3px;font-size:10px;font-weight:700;color:var(--ink);display:flex;align-items:center;justify-content:center}

  .nav{left:0;top:93px;width:900px;height:34px;background:var(--yellow)}
  .nav ul{list-style:none;display:flex;align-items:center;height:34px;padding-left:75px}
  .nav li{font-family:"Ubuntu",sans-serif;font-weight:500;font-size:10.2px;color:#222;padding:0 13px;height:20px;display:flex;align-items:center;border-left:1px solid #c99c06}
  .nav li:nth-child(1),.nav li:nth-child(2){border-left:none}
  .nav li.active{background:var(--blue);color:var(--white);border-radius:3px;padding:0 5px;margin-right:6px}

  .hero{left:0;top:127px;width:900px;height:274px;background:linear-gradient(180deg,#8fb5de 0%,#c7d9ec 30%,#d9c58a 45%,#e3cf8a 70%,#6b7d44 88%,#4f6a30 100%)}

  /* content boxes */
  .box{border:1px solid var(--line);background:var(--white)}
  .welcome{left:75px;top:428px;width:503px;height:152px;padding:10px 6px}
  .welcome h1{font-family:"Ubuntu",sans-serif;font-weight:400;font-size:16px;color:#333;padding-bottom:6px;border-bottom:1px solid #999;width:415px;position:relative}
  .welcome h1 span{color:var(--blue)}
  .welcome h1::after{content:"";position:absolute;left:0;bottom:-2px;width:100px;height:3px;background:#999}
  .welcome p{margin-top:16px;font-size:8.6px;line-height:13.6px;color:var(--ink);padding-left:1px}

  .video{left:610px;top:430px;width:214px;height:149px;background:radial-gradient(circle at 50% 45%,#3a3a3a,#0e0e0e 75%)}
  .video-play{position:absolute;left:84px;top:48px;width:48px;height:36px;background:#1a1a1a;border-radius:3px;display:flex;align-items:center;justify-content:center}
  .video-bar{position:absolute;left:4px;right:4px;bottom:4px;height:14px;background:#f2f2f2;font-size:6.5px;display:flex;align-items:center;gap:6px;padding:0 5px;color:#222}
  .video-bar .track{flex:1;height:3px;background:#999}

  .panel-head{height:29px;background:var(--blue);color:var(--white);font-family:"Ubuntu",sans-serif;font-weight:500;font-size:12.4px;padding:8px 10px}
  .family{left:75px;width:503px}
  .family.one{top:610px;height:209px}
  .family.two{top:847px;height:210px}
  .item{position:absolute;left:7px;display:flex;gap:33px}
  .thumb{width:94px;height:70px;border:3px solid var(--blue)}
  .thumb.agent{background:linear-gradient(135deg,#3f7ec4,#b9d3ee 55%,#e3d8c3)}
  .thumb.globe{background:linear-gradient(180deg,#4f92d6,#cfe3f3 55%,#9ccb5b 80%,#5e9e2e)}
  .item h3{font-family:"Arimo",sans-serif;font-weight:400;font-size:10.4px;color:var(--blue);margin-top:4px}
  .item p{width:295px;font-size:9.4px;line-height:13.6px;margin-top:4px;color:var(--ink)}

  .news{left:610px;top:610px;width:214px;height:209px}
  .news-item{position:absolute;left:7px;display:flex;gap:10px}
  .news-thumb{width:72px;height:50px;background:linear-gradient(180deg,#8db7e0 0%,#d6e4f0 40%,#c9a98a 55%,#6e8b3c 85%)}
  .news-item h4{font-weight:400;font-size:9px;color:var(--blue);margin-top:3px}
  .news-item p{font-size:8.6px;line-height:13.6px;margin-top:2px;width:115px}

  .testimonial{left:610px;top:850px;width:213px;height:183px;border-radius:14px;background:linear-gradient(160deg,#3a7fcf,#1b5aa6 60%,#174f95)}
  .testimonial h2{font-family:"Ubuntu",sans-serif;font-weight:500;font-size:14px;color:var(--yellow);padding:13px 0 0 18px;letter-spacing:.3px}
  .testimonial p{color:var(--white);font-size:9.6px;line-height:16.6px;text-align:justify;padding:6px 22px 0 22px}
  .quote{color:var(--yellow);font-family:"Ubuntu",sans-serif;font-weight:700;font-size:15px;line-height:0}
  .tail{left:754px;top:1030px}

  /* footer */
  .footer{left:0;top:1107px;width:900px;height:93px;background:var(--footer)}
  .contact{position:absolute;left:76px;top:20px;color:var(--white);font-size:10.3px;line-height:15px}
  .social{position:absolute;left:580px;top:10px;display:flex;align-items:center;gap:8px}
  .social h5{font-family:"Ubuntu",sans-serif;font-weight:500;font-size:14px;color:var(--white);margin-right:8px}
  .dot{width:27px;height:27px;border-radius:50%}
  .dot.fb{background:#1f5aa0}.dot.tw{background:#29a8e6}.dot.rss{background:#f39c1d}.dot.mail{background:#d8d8d8;display:flex;align-items:center;justify-content:center}
  .badges{position:absolute;left:482px;top:48px;display:flex;gap:10px;align-items:center}
  .badge{background:#dcdcdc;border-radius:3px}
  .footer-brand{font-family:"Ubuntu",sans-serif;font-weight:700;font-size:9px;color:var(--white);width:44px;line-height:1.1}
</style>
</head>
<body>

<header>
  <div class="abs brand">
    <div class="brand-mark"></div>
    <div class="brand-name">Martin Brantow</div>
  </div>
  <form class="abs signup">
    <div class="signup-field">Your Name</div>
    <div class="signup-field email">Your Email</div>
    <div class="signup-btn">SUBMIT</div>
  </form>
</header>

<nav class="abs nav">
  <ul>
    <li class="active">HOME</li>
    <li>AUCTIONS</li>
    <li>REAL ESTATE LISTINGS</li>
    <li>OUR SERVICES</li>
    <li>WHY AUCTIONS</li>
    <li>ABOUT US</li>
    <li>PAST AUCTIONS</li>
    <li>CONTACT US</li>
  </ul>
</nav>

<div class="abs hero" role="img" aria-label="Slideshow: two-storey yellow stucco house with palm trees under a blue sky"></div>

<section class="abs box welcome">
  <h1><span>WELCOME</span> TO HALLOWELL'S AUCTIONS MART LTD.</h1>
  <p>Lorem Ipsum is that it has a more-or-less normal distribution of letters, as opposed to using 'Content here, content here', making it look like readable English. Many desktop publishing packages and web page editors now use Lorem Ipsum as their default model text, and a search for 'lorem ipsum' will uncover many web sites still in their infancy. Various versions have evolved over the years, sometimes by accident, sometimes on purpose (injected humour and the like</p>
</section>

<section class="abs video" aria-label="Featured video">
  <div class="video-play">
    <svg width="18" height="22" viewBox="0 0 18 22"><path d="M1 1 L17 11 L1 21 Z" fill="#e6e6e6"/></svg>
  </div>
  <div class="video-bar">
    <svg width="6" height="7" viewBox="0 0 6 7"><path d="M0 0 L6 3.5 L0 7Z" fill="#222"/></svg>
    <span>00:00</span><span class="track"></span><span>00:00</span>
    <svg width="16" height="7" viewBox="0 0 16 7"><rect x="0" y="2" width="3" height="3" fill="#222"/><rect x="5" y="4" width="1.5" height="3" fill="#222"/><rect x="8" y="3" width="1.5" height="4" fill="#222"/><rect x="11" y="1" width="1.5" height="6" fill="#222"/><rect x="14" y="0" width="1.5" height="7" fill="#222"/></svg>
    <svg width="7" height="7" viewBox="0 0 7 7"><path d="M0 2V0H2M5 0H7V2M7 5V7H5M2 7H0V5" stroke="#222" fill="none"/></svg>
  </div>
</section>

<section class="abs box family one">
  <div class="panel-head">FAMILY OWNED AND OPERATED WITH A FAMILY GUARANTEE</div>
  <article class="item" style="top:41px">
    <div class="thumb agent" role="img" aria-label="Agent hand holding a house key in front of a home"></div>
    <div><h3>FURNITURE ' ANTIQUES ' COLLECTIBLES</h3><p>Lorem Ipsum is that it has a more-or-less normal distribution of letters, as opposed to using 'Content here, content here', making it look like readable English. Many desktop publishing packages</p></div>
  </article>
  <article class="item" style="top:126px">
    <div class="thumb globe" role="img" aria-label="Open hand holding a glass bubble with a house over a green field"></div>
    <div><h3>FURNITURE ' ANTIQUES ' COLLECTIBLES</h3><p>Lorem Ipsum is that it has a more-or-less normal distribution of letters, as opposed to using 'Content here, content here', making it look like readable English. Many desktop publishing packages</p></div>
  </article>
</section>

<aside class="abs box news">
  <div class="panel-head">NEWS &amp; EVENTS</div>
  <div class="news-item" style="top:37px"><div class="news-thumb" role="img" aria-label="Brick family house"></div><div><h4>SETURDAY MARCH 6, 2014</h4><p>Lorem Ipsum is that it has a more-or-less</p></div></div>
  <div class="news-item" style="top:92px"><div class="news-thumb" role="img" aria-label="Brick family house"></div><div><h4>SETURDAY MARCH 6, 2014</h4><p>Lorem Ipsum is that it has a more-or-less</p></div></div>
  <div class="news-item" style="top:152px"><div class="news-thumb" role="img" aria-label="Brick family house"></div><div><h4>SETURDAY MARCH 6, 2014</h4><p>Lorem Ipsum is that it has a more-or-less</p></div></div>
</aside>

<section class="abs box family two">
  <div class="panel-head">FAMILY OWNED AND OPERATED WITH A FAMILY GUARANTEE</div>
  <article class="item" style="top:41px">
    <div class="thumb agent" role="img" aria-label="Agent hand holding a house key in front of a home"></div>
    <div><h3>FURNITURE ' ANTIQUES ' COLLECTIBLES</h3><p>Lorem Ipsum is that it has a more-or-less normal distribution of letters, as opposed to using 'Content here, content here', making it look like readable English. Many desktop publishing packages</p></div>
  </article>
  <article class="item" style="top:126px">
    <div class="thumb globe" role="img" aria-label="Open hand holding a glass bubble with a house over a green field"></div>
    <div><h3>FURNITURE ' ANTIQUES ' COLLECTIBLES</h3><p>Lorem Ipsum is that it has a more-or-less normal distribution of letters, as opposed to using 'Content here, content here', making it look like readable English. Many desktop publishing packages</p></div>
  </article>
</section>

<aside class="abs testimonial">
  <h2>TESTIMONIALS BLOG</h2>
  <p><span class="quote">&ldquo;</span> simply dummy text of the printing and typesetting industry. Lorem Ipsum has been the industry's standard dummy text ever since the 1500s, when an unknown dummy text ever since printer took a galley of type and scrambled it to make a type. <span class="quote">&rdquo;</span></p>
</aside>
<svg class="abs tail" width="30" height="24" viewBox="0 0 30 24"><path d="M0 0 H28 V23 Z" fill="#174f95"/></svg>

<footer class="abs footer">
  <div class="contact">
    Phone: (270) 555-0148<br>
    Contacts: Martin Brantow<br>
    Email: martinbrantow@mailvex.example<br>
    Address: 482 Wexcombe Lane • Bowling Green, KY 42190
  </div>
  <div class="social">
    <h5>Social Media</h5>
    <span class="dot fb"></span>
    <span class="dot tw"></span>
    <span class="dot rss"></span>
    <span class="dot mail"><svg width="13" height="9" viewBox="0 0 13 9"><rect x=".5" y=".5" width="12" height="8" fill="#fff" stroke="#999"/><path d="M.5 .5 L6.5 5 L12.5 .5" fill="none" stroke="#999"/></svg></span>
  </div>
  <div class="badges">
    <span class="badge" style="width:62px;height:30px;border-radius:15px"></span>
    <span class="badge" style="width:32px;height:36px"></span>
    <span class="badge" style="width:64px;height:24px"></span>
    <span class="badge" style="width:50px;height:24px"></span>
    <span class="badge" style="width:26px;height:30px"></span>
    <span class="footer-brand">Martin Brantow</span>
  </div>
</footer>

</body>
</html>
```